Small Local Computer Shop Website Needed

Im after a new website that goes with my brand logo.
We are a small all family run local computer repair company and would like to drive more business via the site.
I have added my old site and one that was in progress also a Facebook link to give you an idea.

I would like to be able to make it stand out more and be easy to navigate.
I am basically a small computer repair shop, we offer in store repairs and upgrades. We also do call outs to your home or business and we also sell laptops,pcs and peripherals.

We do sell Laptops and pcs and although i don't really want to sell directly from the web it would be nice to be able to show what we have on offer on our site, Roughly 20-30 items generally.

Current site
http://byte-vale.com

New Site
http://byte-vale.com/site/

Facebook
http://www.sociabook.com/pages/Byte-Vale/847315902264710

images and files are available.

Many Thanks
Hugo
Byte Vale

Target Market(s)

I cater for all ages!

Industry/Entity Type

It Company

Number of Pages Required

5+ page

Font styles to use
Sans Serif

Requirements
Must have
• Be nice to keep in theme with my Logo.
• Landing page.
• Contact page
• about us
• Laptops (Displaying products currently for sale in store) Generally 10-20 at a time
• Pcs (Displaying products currently for sale in store)
Nice to have
• i would like and easy way for the customers to navigate to my remote support site. ie.
• https://www.remotorhelp.com/
• Easy link to download there trial off shieldwarren antivirus.
• ie http://downloads.shieldwarren.com/partners/rskit/ShieldWarrenDownloader_bytevalekit.exe
• Link to our Repair tracker... When we check in a computer or laptop repair the Customers can see how there jobs progressing by clicking the link. ie http://byte-vale.com/shop/repairstatus/
• would be great if there was a fairly straight forward way to add/ remove pc's and laptops for sale on our site.
• Maybe check our facebook for ideas images etc..
• https://www.sociabook.com/Byte-vale-847315902264710/
Should not have
• The site i currently have i really dislike, so please dont copy that theme.
• Had a few designs with a white banner at the top with my logo.
• Sorry but have decided these are not what i want.
• a darker theme is def more in line with what im looking for.
• Thanks

```html
<!DOCTYPE html>
<html lang="en">
<head>
<meta charset="utf-8">
<title>Byte Vale – Local Computer Repair Specialists</title>
<link href="https://fonts.googleapis.com/css2?family=Montserrat:wght@400;600;700&family=Raleway:wght@400;500;600&family=Lora:ital@1&display=swap" rel="stylesheet">
<style>
:root{
  --bg-top:#161616;
  --bg-nav:#1d1d1d;
  --bg-welcome:#262626;
  --bg-clients:#1e1e1e;
  --bg-offer:#232323;
  --bg-voucher:#1c1c1c;
  --bg-footer:#111111;
  --accent:#1f86b3;
  --accent-light:#2aa9d8;
  --accent-pale:#7fb2c4;
  --tile:#3a3a3a;
  --text:#ffffff;
  --muted:#9a9a9a;
  --dim:#5f5f5f;
  --price:#d0312d;
}
*{margin:0;padding:0;box-sizing:border-box}
html,body{width:1200px;height:2927px;overflow:hidden;background:var(--bg-footer)}
body{font-family:"Raleway",sans-serif;color:var(--text);position:relative}
.abs{position:absolute}
section,header,footer{position:absolute;left:0;width:1200px}
.heading{font-family:"Montserrat",sans-serif;font-weight:700;text-transform:uppercase;font-size:22px;letter-spacing:.5px}
.subheading{font-family:"Montserrat",sans-serif;font-size:12px;text-transform:uppercase;letter-spacing:1px;margin-top:4px}
.btn{position:absolute;display:flex;align-items:center;justify-content:center;border-radius:16px;font-family:"Montserrat",sans-serif;font-size:10px;text-transform:uppercase;letter-spacing:1px;color:#fff;white-space:nowrap}

/* top bar */
.topbar{top:0;height:39px;background:var(--bg-top);font-size:9px;text-transform:uppercase;letter-spacing:1px;color:#cfcfcf}
.topbar .welcome{left:172px;top:14px}
.topbar .contact-item{top:12px;display:flex;align-items:center;gap:8px}

/* nav */
.nav{top:39px;height:55px;background:var(--bg-nav)}
.logo{font-family:"Montserrat",sans-serif;font-weight:700;font-size:24px;color:#fff;display:flex;align-items:center;gap:8px;white-space:nowrap}
.nav .logo{left:158px;top:14px}
.menu{position:absolute;left:524px;top:22px;width:370px;display:flex;justify-content:space-between;font-family:"Montserrat",sans-serif;font-size:9.5px;text-transform:uppercase;letter-spacing:.8px;color:#cfcfcf;white-space:nowrap}
.menu .active{color:var(--accent-light)}
.nav .btn{left:921px;top:13px;width:106px;height:29px;background:var(--accent-light)}

/* hero */
.hero{top:94px;height:563px;background:linear-gradient(90deg,#4a4d52 0%,#6a6c70 30%,#2f3136 55%,#7b7e82 85%,#5b5e62 100%)}
.hero::after{content:"";position:absolute;inset:0;background:rgba(0,0,0,.25)}
.hero h1{position:absolute;left:0;width:1200px;top:222px;text-align:center;font-family:"Montserrat",sans-serif;font-weight:700;font-size:37px;line-height:44px;text-transform:uppercase;z-index:2;text-shadow:0 2px 4px rgba(0,0,0,.4)}
.hero .dots{position:absolute;left:578px;top:517px;display:flex;gap:6px;z-index:2}
.hero .dots span{width:11px;height:11px;border-radius:50%;border:2px solid #ddd}
.hero .dots .on{background:#fff}

/* welcome */
.welcome-section{top:657px;height:543px;background:var(--bg-welcome)}
.welcome-section .intro{left:172px;top:74px;width:470px}
.welcome-section .intro p{margin-top:30px;font-size:11.5px;line-height:20px;color:#b5b5b5}
.shop-photo{left:172px;top:268px;width:439px;height:224px;background:linear-gradient(180deg,#5c6672 0%,#8a8f94 40%,#4e4a46 100%)}
.feature{position:absolute;left:685px;width:360px;height:90px}
.feature .icon{position:absolute;left:0;top:2px;width:50px;height:50px;background:var(--tile);display:flex;align-items:center;justify-content:center}
.feature .icon.blue{background:var(--accent)}
.feature h3{position:absolute;left:72px;top:0;font-family:"Raleway",sans-serif;font-weight:500;font-size:14px;letter-spacing:.3px;white-space:nowrap}
.feature h3.caps{text-transform:uppercase}
.feature p{position:absolute;left:72px;top:22px;width:275px;font-size:10.5px;line-height:17px;color:#a5a5a5}

/* clients */
.clients{top:1200px;height:332px;background:var(--bg-clients)}
.car-photo{left:590px;top:20px;width:620px;height:300px;border-radius:200px 220px 40px 40px;background:radial-gradient(ellipse at 50% 45%,#3b3e43 0%,#2a2c30 55%,rgba(30,30,30,0) 75%)}
.clients .title{left:172px;top:66px}
.quote-mark{left:170px;top:135px;font-family:"Lora",serif;font-size:70px;line-height:70px;color:#8a8a8a}
.quote{left:246px;top:140px;width:400px;font-family:"Lora",serif;font-style:italic;font-size:11.5px;line-height:20px;color:#cfcfcf}
.byline{left:246px;top:236px;font-size:9.5px;text-transform:uppercase;color:#9a9a9a;line-height:17px}
.byline b{color:var(--accent-light);font-weight:500}
.divider-v{left:661px;top:122px;width:2px;height:152px;background:#aaa}
.avatar{position:absolute;top:140px;width:98px;height:98px;border-radius:50%;border:4px solid #222}
.client-dots{left:838px;top:254px;display:flex;gap:6px}
.client-dots span{width:9px;height:9px;border-radius:50%;background:#ddd}
.client-dots .on{background:var(--accent-light)}

/* offer */
.offer{top:1532px;height:907px;background:var(--bg-offer)}
.offer .title{left:172px;top:40px}
.offer .btn{left:907px;top:44px;width:119px;height:28px;background:var(--accent-light)}
.service{position:absolute;width:280px;height:100px}
.service .icon{position:absolute;left:0;top:0;width:50px;height:50px;background:var(--tile);display:flex;align-items:center;justify-content:center}
.service .icon.blue{background:var(--accent)}
.service h3{position:absolute;left:72px;top:0;font-weight:500;font-size:14px;white-space:nowrap}
.service p{position:absolute;left:72px;top:22px;width:200px;font-size:10.5px;line-height:17px;color:var(--dim)}
.products-title{left:0;width:1200px;top:435px;text-align:center}
.product{position:absolute;top:517px;width:200px;height:302px;background:#2d2d2d}
.product .shot{position:absolute;left:10px;top:10px;width:180px;height:172px;background:radial-gradient(circle at 50% 50%,#ffffff 0%,#e6e6e6 70%,#cfcfcf 100%)}
.product .shot .device{position:absolute;left:45px;top:50px;width:90px;height:62px;border-radius:3px;background:linear-gradient(135deg,#3a3f47,#1c1f24)}
.product h4{position:absolute;left:0;width:200px;top:195px;text-align:center;font-weight:600;font-size:13px;line-height:19px}
.product .price{position:absolute;left:0;width:200px;top:233px;text-align:center;font-size:13px;color:var(--price);font-weight:600}
.product .btn{left:50px;top:263px;width:100px;height:28px;border-radius:0;background:var(--accent);text-transform:none;letter-spacing:0;font-family:"Raleway",sans-serif;font-size:11px}
.arrow{position:absolute;top:638px}

/* voucher */
.voucher{top:2439px;height:209px;background:var(--bg-voucher);text-align:center}
.voucher h2{position:absolute;left:0;width:1200px;top:58px;font-weight:500;font-size:24px}
.voucher p{position:absolute;left:0;width:1200px;top:92px;font-family:"Montserrat",sans-serif;font-size:9px;text-transform:uppercase;letter-spacing:.5px}
.voucher .more{left:487px;top:125px;width:106px;height:28px;background:var(--accent)}
.voucher .contact{left:607px;top:125px;width:106px;height:28px;background:var(--accent-pale)}

/* footer */
.footer{top:2648px;height:279px;background:var(--bg-footer)}
.footer .logo{left:160px;top:76px}
.footer h5{font-weight:500;font-size:14px;margin-bottom:18px}
.footer ul{list-style:none;font-size:9.5px;text-transform:uppercase;letter-spacing:1px;color:#cfcfcf;line-height:27px;white-space:nowrap}
.col{position:absolute;top:46px}
.newsletter-note{font-size:9.5px;text-transform:uppercase;letter-spacing:1px;color:#cfcfcf}
.signup{display:flex;margin-top:17px;width:197px;height:30px}
.signup .field{flex:1;background:#0a0a0a;border:1px solid #444;font-size:8.5px;text-transform:uppercase;color:#bbb;padding:10px 8px}
.signup .go{width:30px;background:var(--accent);font-size:10px;display:flex;align-items:center;justify-content:center}
.socials{display:flex;gap:12px;margin-top:6px}
.footer .rule{left:200px;top:234px;width:800px;height:1px;background:#2e2e2e}
.footer .copy{left:0;width:1200px;top:250px;text-align:center;font-size:9px;text-transform:uppercase;letter-spacing:1px;color:#cfcfcf}
</style>
</head>
<body>

<header class="topbar">
  <span class="abs welcome">Welcome to our site</span>
  <span class="abs contact-item" style="left:757px">
    <svg width="9" height="14" viewBox="0 0 9 14"><rect x="1" y="1" width="7" height="12" rx="1.5" fill="none" stroke="#ccc" stroke-width="1.3"/></svg>+44 1600 555 014</span>
  <span class="abs contact-item" style="left:896px">
    <svg width="14" height="10" viewBox="0 0 14 10"><rect x="1" y="1" width="12" height="8" fill="none" stroke="#ccc" stroke-width="1.2"/><path d="M1 1l6 5 6-5" fill="none" stroke="#ccc" stroke-width="1.2"/></svg>sales@byte-vale.com</span>
</header>

<header class="nav">
  <div class="abs logo">Byte Vale</div>
  <nav class="menu">
    <span class="active">Home</span><span>About us</span><span>Store</span><span>Gallery</span><span>Service</span><span>Blog</span>
  </nav>
  <span class="btn">Contact us</span>
</header>

<section class="hero">
  <div class="abs" style="inset:0" role="img" aria-label="Photo of the shop interior with a service counter and shelves of computer accessories"></div>
  <h1>Byte Vale are a highly professional<br>local repair specialists</h1>
  <div class="dots"><span></span><span></span><span class="on"></span></div>
</section>

<section class="welcome-section">
  <div class="abs intro">
    <h2 class="heading">Welcome to our site</h2>
    <div class="subheading">About us</div>
    <p>Valeford's No 1 Computer Repair Shop and callout service covering over a 25 mile radius from our base in Valeford. We offer a wide range of services. Setting up broadband, wireless networks, hardware \ software issue, PC clean up, data recovery, virus and spyware removal. Byte Vale are a highly professional local repair specialists based in Valeford, Coombshire. We have been trading since 2004, Read More....</p>
  </div>
  <div class="abs shop-photo" role="img" aria-label="Photo of the shop front with its sign above the glass door"></div>

  <div class="feature" style="top:80px">
    <div class="icon blue"><svg width="18" height="18" viewBox="0 0 18 18"><circle cx="3" cy="15" r="2.2" fill="#fff"/><path d="M1 8a9 9 0 0 1 9 9M1 2a15 15 0 0 1 15 15" fill="none" stroke="#fff" stroke-width="2.4"/></svg></div>
    <h3 class="caps">Broadband &amp; Wireless</h3>
    <p>Setting up any network can be a tricky task, so why not get a bit of assistance to make sure you have the freedom and the security you need.</p>
  </div>
  <div class="feature" style="top:190px">
    <div class="icon"><svg width="22" height="16" viewBox="0 0 22 16"><rect x="4" y="2" width="14" height="9" fill="none" stroke="#fff" stroke-width="1.6"/><path d="M1 13h20" stroke="#fff" stroke-width="2"/></svg></div>
    <h3 class="caps">Hardware / Software Issues</h3>
    <p>We all know that sometime PCs and MACs like to have their off days. We are here to help out on such occasions. No problem to big no software bug too small.</p>
  </div>
  <div class="feature" style="top:299px">
    <div class="icon"><svg width="18" height="20" viewBox="0 0 18 20"><rect x="2" y="9" width="14" height="10" fill="#fff"/><path d="M5 9V5a4 4 0 0 1 8 0" fill="none" stroke="#fff" stroke-width="2"/></svg></div>
    <h3 class="caps">Byte Vale</h3>
    <p>Computers, like cars, need to have a regular service and mot. We offer a full mot on your computer, from health check on all hardware, any software issues, and even clean the dust out of your machine.</p>
  </div>
  <div class="feature" style="top:410px">
    <div class="icon"><svg width="20" height="20" viewBox="0 0 20 20"><ellipse cx="10" cy="11" rx="4.5" ry="6" fill="#fff"/><path d="M2 6l4 3M18 6l-4 3M1 12h4M19 12h-4M3 18l3-3M17 18l-3-3M7 3l1.5 2M13 3l-1.5 2" stroke="#fff" stroke-width="1.6"/></svg></div>
    <h3>Virus &amp; Spyware Issues</h3>
    <p>We all know how amazing and powerful the internet is but sadly viruses and spyware like to wriggle around. We can clean all computers to get you back online.</p>
  </div>
</section>

<section class="clients">
  <div class="abs car-photo" role="img" aria-label="Faded photo of the branded service car"></div>
  <div class="abs title">
    <h2 class="heading">Clients</h2>
    <div class="subheading">Customers says about us</div>
  </div>
  <div class="abs quote-mark">&ldquo;</div>
  <p class="abs quote">Lorem Ipsum is simply dummy text of the printing and typesetting industry. Lorem Ipsum has been the industry's standard dummy text ever since the 1500s, when an unknown printer took a galley of type and scrambled it to make a type specimen book. It has survived not only five centuries.</p>
  <div class="abs byline">By<br><b>Martin Ellory</b></div>
  <div class="abs divider-v"></div>
  <div class="avatar" style="left:686px;background:linear-gradient(135deg,#e9b15a,#a7652e)" role="img" aria-label="Portrait of a smiling customer"></div>
  <div class="avatar" style="left:806px;background:linear-gradient(135deg,#8a5a3c,#3f2a22)" role="img" aria-label="Portrait of a customer"></div>
  <div class="avatar" style="left:926px;background:linear-gradient(135deg,#a0654a,#3a2420)" role="img" aria-label="Portrait of a customer in a suit"></div>
  <div class="abs client-dots"><span class="on"></span><span></span><span></span></div>
</section>

<section class="offer">
  <div class="abs title">
    <h2 class="heading">What we offer!</h2>
    <div class="subheading">Lorem ipsum dolor</div>
  </div>
  <span class="btn">Learn more</span>

  <div class="service" style="left:172px;top:130px">
    <div class="icon blue"><svg width="20" height="20" viewBox="0 0 20 20"><path d="M3 17l8-8" stroke="#fff" stroke-width="3" stroke-linecap="round"/><circle cx="13.5" cy="6.5" r="4" fill="none" stroke="#fff" stroke-width="2.4"/></svg></div>
    <h3>Dc Jack Repair</h3>
    <p>Lorem Ipsum is simply dummy text of the printing and typesetting industry. Lorem Ipsum has been.</p>
  </div>
  <div class="service" style="left:464px;top:130px">
    <div class="icon"><svg width="20" height="18" viewBox="0 0 20 18"><path d="M2 9h9M8 5l4 4-4 4" fill="none" stroke="#fff" stroke-width="2.2"/><path d="M12 2h6v14h-6" fill="none" stroke="#fff" stroke-width="2"/></svg></div>
    <h3>Windows Installation</h3>
    <p>Lorem Ipsum is simply dummy text of the printing and typesetting industry. Lorem Ipsum has been.</p>
  </div>
  <div class="service" style="left:757px;top:130px">
    <div class="icon"><svg width="20" height="20" viewBox="0 0 20 20"><ellipse cx="10" cy="11" rx="4.5" ry="6" fill="#fff"/><path d="M2 6l4 3M18 6l-4 3M1 12h4M19 12h-4M3 18l3-3M17 18l-3-3" stroke="#fff" stroke-width="1.6"/></svg></div>
    <h3>Virus Removal</h3>
    <p>Lorem Ipsum is simply dummy text of the printing and typesetting industry. Lorem Ipsum has been.</p>
  </div>
  <div class="service" style="left:172px;top:247px">
    <div class="icon"><svg width="16" height="20" viewBox="0 0 16 20"><path d="M1 1h9l5 5v13H1z" fill="none" stroke="#fff" stroke-width="1.8"/><path d="M4 10h8M4 13h8M4 16h8" stroke="#fff" stroke-width="1.4"/></svg></div>
    <h3>Data Recovery</h3>
    <p>Lorem Ipsum is simply dummy text of the printing and typesetting industry. Lorem Ipsum has been.</p>
  </div>
  <div class="service" style="left:464px;top:247px">
    <div class="icon"><svg width="14" height="22" viewBox="0 0 14 22"><rect x="1" y="1" width="12" height="20" rx="2" fill="none" stroke="#fff" stroke-width="1.8"/><path d="M4 8l3 3-3 3M8 14h3" fill="none" stroke="#fff" stroke-width="1.4"/></svg></div>
    <h3>Screen Repairs</h3>
    <p>Lorem Ipsum is simply dummy text of the printing and typesetting industry. Lorem Ipsum has been.</p>
  </div>
  <div class="service" style="left:757px;top:247px">
    <div class="icon"><svg width="22" height="16" viewBox="0 0 22 16"><rect x="4" y="2" width="14" height="9" fill="none" stroke="#fff" stroke-width="1.6"/><path d="M1 13h20" stroke="#fff" stroke-width="2"/></svg></div>
    <h3>Laptop &amp; PC Sale</h3>
    <p>Lorem Ipsum is simply dummy text of the printing and typesetting industry. Lorem Ipsum has been.</p>
  </div>

  <div class="abs products-title">
    <h2 class="heading">Some of our products</h2>
    <div class="subheading">Lorem ipsum dolor</div>
  </div>

  <svg class="arrow" style="left:103px" width="26" height="56" viewBox="0 0 26 56"><path d="M24 2L2 28l22 26" fill="none" stroke="#bbb" stroke-width="1.5"/></svg>
  <svg class="arrow" style="left:1066px" width="26" height="56" viewBox="0 0 26 56"><path d="M2 2l22 26L2 54" fill="none" stroke="#bbb" stroke-width="1.5"/></svg>

  <div class="product" style="left:172px">
    <div class="shot" role="img" aria-label="Photo of a laptop with a colourful screen"><div class="device"></div></div>
    <h4>Vestibulum vitae metus ut<br>arcu commodo</h4><div class="price">$294.00</div><span class="btn">More Details</span>
  </div>
  <div class="product" style="left:389px">
    <div class="shot" role="img" aria-label="Photo of a desktop PC with monitor, keyboard and mouse"><div class="device"></div></div>
    <h4>Vestibulum vitae metus ut<br>arcu commodo</h4><div class="price">$294.00</div><span class="btn">More Details</span>
  </div>
  <div class="product" style="left:607px">
    <div class="shot" role="img" aria-label="Photo of a silver laptop"><div class="device"></div></div>
    <h4>Vestibulum vitae metus ut<br>arcu commodo</h4><div class="price">$294.00</div><span class="btn">More Details</span>
  </div>
  <div class="product" style="left:824px">
    <div class="shot" role="img" aria-label="Photo of a gaming PC tower with monitor"><div class="device"></div></div>
    <h4>Vestibulum vitae metus ut<br>arcu commodo</h4><div class="price">$294.00</div><span class="btn">More Details</span>
  </div>
</section>

<section class="voucher">
  <h2>Exclusive 10% OFF Instore Voucher</h2>
  <p>Lorem ipsum is simply dummy text of the printing and typesetting.</p>
  <span class="btn more">More</span>
  <span class="btn contact">Contact us</span>
</section>

<footer class="footer">
  <div class="abs logo">Byte Vale</div>
  <div class="col" style="left:318px">
    <h5>Menu</h5>
    <ul><li>Home</li><li>About us</li><li>Features</li><li>Portfolio</li></ul>
  </div>
  <div class="col" style="left:464px">
    <h5>&nbsp;</h5>
    <ul><li>Service</li><li>Blog</li><li>Blog pages</li></ul>
    <div class="socials">
      <svg width="8" height="12" viewBox="0 0 8 12"><rect x="2" y="1" width="4" height="10" fill="#ccc"/></svg>
      <svg width="10" height="12" viewBox="0 0 10 12"><circle cx="5" cy="6" r="4" fill="#ccc"/></svg>
      <svg width="10" height="12" viewBox="0 0 10 12"><rect x="1" y="2" width="8" height="8" fill="#ccc"/></svg>
    </div>
  </div>
  <div class="col" style="left:587px">
    <h5>Contact</h5>
    <ul><li>Address : 12 Alder Row, Valeford,</li><li>Coombshire, VF2 6QT</li><li>Phone : 01600 555 014</li><li>Email : sales@byte-vale.com</li></ul>
  </div>
  <div class="col" style="left:829px">
    <h5>Newsletter</h5>
    <div class="newsletter-note">Sign up your newsletter</div>
    <div class="signup"><span class="field">Email address</span><span class="go">GO</span></div>
  </div>
  <div class="abs rule"></div>
  <div class="abs copy">&copy; 2016 yoursite. allright reserved</div>
</footer>

</body>
</html>
```